MAREK DOLVANE FOR CONGRESS DISTRICT 32

I need to create a campaign flyer for my congress campaign. I am running for congress in District 32 of Texas as a republican. I am a former Olympic athlete, world champion fencer, Army veteran, Counterintelligence officer (I catch spies).
I want just my first name MAREK in big letters at the top. I want it to say MAREK and below it Republican for Congress.
www.marekforcongress.example

Industry/Entity Type

Political

Colors
EB3D1F
EC4F4E
F09395
F8D3D4
FCEDEE

Requirements
Nice to have
• Would love a catchy title for the Flyer like "Spy Catcher", "Olympic Athlete" "World Champion Fencer" running for Congress in your District!

```html
<!DOCTYPE html>
<html lang="en">
<head>
<meta charset="utf-8">
<title>Marek Dolvane for Congress District 32</title>
<link rel="stylesheet" href="https://fonts.googleapis.com/css2?family=Montserrat:wght@500;600;700;800;900&display=swap">
<style>
  :root {
    --stage: #a7a8ab;
    --banner-light: #d4d5d7;
    --banner-dark: #55565a;
    --navy-deep: #0e1845;
    --navy: #1e2d66;
    --navy-bright: #1a4a8f;
    --red: #e8233d;
    --red-dark: #a51d2b;
    --white: #ffffff;
    --photo-light: #eef0f3;
    --photo-mid: #c9ced6;
  }
  * { margin: 0; padding: 0; box-sizing: border-box; }
  html, body { width: 919px; height: 1200px; overflow: hidden; }
  body {
    background: var(--stage);
    font-family: "Montserrat", Arial, sans-serif;
    position: relative;
  }
  .title-banner {
    position: absolute; left: 0; top: 27px; width: 919px; height: 73px;
    background: linear-gradient(90deg, var(--banner-light) 0%, #9a9b9e 45%, var(--banner-dark) 100%);
    display: flex; align-items: center; justify-content: center;
  }
  .title-banner h1 {
    color: var(--white); font-weight: 600; font-size: 25px; letter-spacing: 0.3px;
  }
  .flyer {
    position: absolute; left: 112px; top: 132px; width: 695px; height: 981px;
    background: var(--white); overflow: hidden;
    box-shadow: 0 4px 18px rgba(0,0,0,0.25);
  }
  .flyer > * { position: absolute; }
  .star-band {
    left: 0; top: 0; width: 695px; height: 106px;
    background: linear-gradient(90deg, var(--navy-deep), var(--navy-bright));
  }
  .star-band svg { position: absolute; left: 0; top: 0; }
  .vote-tag {
    left: 244px; top: 82px; width: 207px; height: 43px;
    background: var(--red); border-bottom: 3px solid var(--red-dark);
    color: var(--white); font-weight: 800; font-size: 32px;
    display: flex; align-items: center; justify-content: center; line-height: 1;
    z-index: 2;
  }
  .candidate-name { left: 77px; top: 132px; }
  .party-tag {
    left: 77px; top: 291px; width: 535px; height: 41px;
    background: var(--red); border-bottom: 3px solid var(--red-dark);
    color: var(--white); font-size: 28px; font-weight: 800;
    display: flex; align-items: center; justify-content: center; line-height: 1;
  }
  .party-tag .light { font-weight: 500; margin: 0 8px; }
  .flag-art {
    left: 110px; top: 333px; width: 456px; height: 148px;
    background: linear-gradient(90deg, #1f3578 0%, #3a56a0 50%, #e36a6a 62%, #f2b3a8 100%);
    opacity: 0.9;
  }
  .portrait {
    left: 394px; top: 328px; width: 271px; height: 393px;
    background: radial-gradient(ellipse at 50% 45%, var(--photo-mid) 0%, var(--photo-light) 60%, rgba(255,255,255,0) 100%);
  }
  .headline { left: 0; top: 0; width: 0; height: 0; z-index: 2; }
  .headline span {
    position: absolute; color: var(--red); font-weight: 900; line-height: 1; white-space: nowrap;
  }
  .headline .big { left: 64px; top: 483px; font-size: 158px; letter-spacing: -6px; }
  .headline .sub { left: 66px; top: 621px; font-size: 62px; letter-spacing: -1.5px; }
  .district {
    left: 69px; top: 685px; line-height: 1; color: var(--navy);
    font-weight: 800; font-size: 32px; letter-spacing: -0.5px; z-index: 2;
  }
  .credential {
    height: 66px; background: var(--navy); border-left: 6px solid var(--red);
    color: var(--white); font-weight: 800; font-size: 19px; line-height: 1.3;
    padding-left: 14px; display: flex; align-items: center; text-transform: uppercase;
  }
  .credential.left { left: 69px; width: 182px; }
  .credential.right { left: 298px; width: 326px; padding-left: 17px; }
  .credential.row1 { top: 732px; }
  .credential.row2 { top: 814px; }
  .credential-star { width: 62px; height: 70px; }
  .footer-band {
    left: 0; top: 890px; width: 695px; height: 91px;
    background: linear-gradient(90deg, var(--red) 0%, var(--red) 55%, var(--red-dark) 100%);
    clip-path: polygon(0 25%, 8% 14%, 18% 22%, 30% 8%, 42% 20%, 55% 6%, 66% 18%, 78% 10%, 90% 20%, 100% 12%, 100% 100%, 0 100%);
  }
  .website {
    left: 0; top: 925px; width: 695px; text-align: center; line-height: 1;
    color: var(--white); font-weight: 800; font-size: 28px; letter-spacing: 1px;
  }
</style>
</head>
<body>
  <header class="title-banner"><h1>MAREK DOLVANE FOR CONGRESS DISTRICT 32</h1></header>

  <main class="flyer">
    <div class="star-band">
      <svg width="695" height="106" viewBox="0 0 695 106">
        <defs>
          <polygon id="band-star" points="0,-21 4.9,-6.7 20,-6.5 8,2.6 12.3,17 0,8.4 -12.3,17 -8,2.6 -20,-6.5 -4.9,-6.7" fill="#fff"/>
        </defs>
        <use href="#band-star" x="83" y="45"/>
        <use href="#band-star" x="171" y="45"/>
        <use href="#band-star" x="259" y="45"/>
        <use href="#band-star" x="347" y="45"/>
        <use href="#band-star" x="435" y="45"/>
        <use href="#band-star" x="523" y="45"/>
        <use href="#band-star" x="611" y="45"/>
      </svg>
    </div>

    <div class="vote-tag">VOTE FOR</div>

    <svg class="candidate-name" width="535" height="156" viewBox="0 0 535 156">
      <defs>
        <linearGradient id="name-fill" x1="0" y1="0" x2="0" y2="1">
          <stop offset="0" stop-color="#1a4a8f"/>
          <stop offset="0.55" stop-color="#1e2a63"/>
          <stop offset="1" stop-color="#2a2f82"/>
        </linearGradient>
      </defs>
      <text x="0" y="149" textLength="535" lengthAdjust="spacingAndGlyphs"
            font-family="Montserrat, Arial, sans-serif" font-weight="900" font-size="207"
            fill="url(#name-fill)">MAREK</text>
    </svg>

    <div class="party-tag">REPUBLICAN<span class="light">FOR</span>CONGRESS</div>

    <div class="flag-art" role="img" aria-label="Distressed American flag artwork"></div>
    <div class="portrait" role="img" aria-label="Portrait photo of the candidate in a white shirt"></div>

    <h2 class="headline"><span class="big">SPY</span><span class="sub">CATCHER</span></h2>
    <p class="district">Congress, District 32, Texas</p>

    <div class="credential left row1">Olympic<br>Athlete</div>
    <div class="credential right row1">World Champion<br>Fencer</div>
    <div class="credential left row2">Army<br>Veteran</div>
    <div class="credential right row2">Counterintelligence<br>Officer</div>

    <svg class="credential-star" style="left:210px;top:729px" viewBox="-32 -36 64 72"><polygon points="0,-32 7.5,-10 31,-10 12,4 19,26 0,13 -19,26 -12,4 -31,-10 -7.5,-10" transform="rotate(14)" fill="#fff" stroke="#e8233d" stroke-width="3"/></svg>
    <svg class="credential-star" style="left:585px;top:729px" viewBox="-32 -36 64 72"><polygon points="0,-32 7.5,-10 31,-10 12,4 19,26 0,13 -19,26 -12,4 -31,-10 -7.5,-10" transform="rotate(14)" fill="#fff" stroke="#e8233d" stroke-width="3"/></svg>
    <svg class="credential-star" style="left:210px;top:811px" viewBox="-32 -36 64 72"><polygon points="0,-32 7.5,-10 31,-10 12,4 19,26 0,13 -19,26 -12,4 -31,-10 -7.5,-10" transform="rotate(14)" fill="#fff" stroke="#e8233d" stroke-width="3"/></svg>
    <svg class="credential-star" style="left:585px;top:811px" viewBox="-32 -36 64 72"><polygon points="0,-32 7.5,-10 31,-10 12,4 19,26 0,13 -19,26 -12,4 -31,-10 -7.5,-10" transform="rotate(14)" fill="#fff" stroke="#e8233d" stroke-width="3"/></svg>

    <div class="footer-band"></div>
    <p class="website">WWW.MAREKFORCONGRESS.EXAMPLE</p>
  </main>
</body>
</html>
```